Worksheet for a seminar - wheel of wellbeing

I need a 1 page worksheet for a course I am running next week.
1. The worksheet is based is designed to tie into Valdoric who use 4 colours per specific quadrants - Blue top left, Yellow top right, Green bottom left, Red bottom right. As this is designed to be written and to be printed, it may need to be pale colours however I am open to the correct colours with the image on top if necessary

2. The wellbeing wheel needs to be a design of it's own as it will be used in other things. I would like to have a format for the base wheel that can be changed by me (Only the title names)

3. I have provided the 2 business logo's - these down need to be too big

I hope this helps.

Target Market(s)

Corporate managers and staff - worksheet being used in a workshop

Industry/Entity Type

Wheel

Colors

Designer to choose colors to be used in the design.

Requirements
Must have
• A professional looking wheel that can be used for other purposes. I want to be able to change the 'pie' titles. I will also require a A4 size of the wheel with blank spaces for titles
Nice to have
• A modern feel

```html
<!DOCTYPE html>
<html lang="en">
<head>
<meta charset="utf-8">
<title>Wheel of Wellbeing – Worksheet</title>
<link rel="stylesheet" href="https://fonts.googleapis.com/css2?family=Raleway:wght@200;300;400&family=Montserrat:wght@400;600;800&family=Roboto+Slab:wght@700&display=swap">
<style>
  :root {
    --ink: #333333;
    --title-grey: #8a8a8a;
    --panel: #efefef;
    --field: #ffffff;
    --blue: #33a3d6;
    --yellow: #f4b42b;
    --green: #a5cd39;
    --red: #d2232a;
    --seg-physical: #f5c718;
    --seg-emotional: #a6ce39;
    --seg-spiritual: #f58220;
    --seg-love: #3cb54a;
    --seg-family: #e3222a;
    --seg-social: #93268f;
    --seg-growth: #c49a6c;
    --seg-business: #0b9ad7;
    --spoke: #c4c4c4;
  }
  * { box-sizing: border-box; margin: 0; padding: 0; }
  html, body { width: 849px; height: 1200px; overflow: hidden; background: #fff; }
  body { position: relative; font-family: "Raleway", sans-serif; color: var(--ink); }

  .sheet-title {
    position: absolute; top: 72px; left: 0; width: 849px; text-align: center;
    font-family: "Raleway", sans-serif; font-weight: 200; font-size: 44px; color: var(--title-grey);
  }
  .sheet-subtitle {
    position: absolute; top: 132px; left: 0; width: 849px; text-align: center;
    font-family: "Raleway", sans-serif; font-weight: 400; font-size: 13px; letter-spacing: 3.4px;
  }

  .quadrant { position: absolute; background: var(--panel); }
  .quadrant--assess   { left: 47px;  top: 183px; width: 377px; height: 450px; border-top-left-radius: 30px; }
  .quadrant--goals    { left: 436px; top: 183px; width: 377px; height: 450px; border-top-right-radius: 30px; }
  .quadrant--action   { left: 47px;  top: 646px; width: 377px; height: 444px; border-bottom-left-radius: 34px; }
  .quadrant--reflect  { left: 436px; top: 646px; width: 377px; height: 444px; border-bottom-right-radius: 34px; }

  .quadrant__header {
    position: relative; height: 67px; color: #fff;
  }
  .quadrant--assess .quadrant__header  { background: var(--blue);   border-top-left-radius: 30px; }
  .quadrant--goals .quadrant__header   { background: var(--yellow); border-top-right-radius: 30px; }
  .quadrant--action .quadrant__header  { background: var(--green); }
  .quadrant--reflect .quadrant__header { background: var(--red); }

  .quadrant__icon { position: absolute; left: 14px; top: 10px; width: 50px; height: 50px; }
  .quadrant__heading {
    position: absolute; left: 86px; top: 14px;
    font-family: "Montserrat", sans-serif; font-weight: 800; font-size: 20px; letter-spacing: 0.2px;
  }
  .quadrant__prompt {
    position: absolute; left: 86px; top: 41px;
    font-family: "Raleway", sans-serif; font-weight: 300; font-size: 13px;
  }

  .wheel { position: absolute; left: 19px; top: 88px; width: 340px; height: 340px; }

  .field-label { position: absolute; font-size: 11.5px; font-weight: 400; }
  .field { position: absolute; background: var(--field); border-radius: 7px; }

  .partner { position: absolute; top: 1122px; display: flex; align-items: center; gap: 7px;
    font-family: "Montserrat", sans-serif; font-weight: 600; font-size: 17px; }
  .partner--thrive { left: 520px; color: #3aa98a; }
  .partner--brightpath { left: 680px; color: #7fb33a; }
  .partner__dot { width: 14px; height: 14px; border-radius: 50%; background: currentColor; }
</style>
</head>
<body>

<svg width="0" height="0" style="position:absolute" aria-hidden="true">
  <defs>
    <path id="label-track" d="M0,-150 A150,150 0 1,1 0,150 A150,150 0 1,1 0,-150"/>
    <g id="spoke">
      <line x1="0" y1="0" x2="142" y2="0" stroke="var(--spoke)" stroke-width="0.8"/>
      <line x1="62" y1="-4" x2="62" y2="4" stroke="#9a9a9a" stroke-width="1.2"/>
      <line x1="124" y1="-4" x2="124" y2="4" stroke="#9a9a9a" stroke-width="1.2"/>
      <text x="66" y="-6" font-size="6" fill="#9a9a9a" font-family="Montserrat, sans-serif">5</text>
      <text x="128" y="-6" font-size="6" fill="#9a9a9a" font-family="Montserrat, sans-serif">10</text>
    </g>
    <symbol id="wellbeing-wheel" viewBox="-170 -170 340 340">
      <circle r="142" fill="#fff"/>
      <g fill="none" stroke-width="25">
        <circle r="154" pathLength="360" stroke-dasharray="44 316" stroke="var(--seg-physical)"  transform="rotate(-89.5)"/>
        <circle r="154" pathLength="360" stroke-dasharray="44 316" stroke="var(--seg-emotional)" transform="rotate(-44.5)"/>
        <circle r="154" pathLength="360" stroke-dasharray="44 316" stroke="var(--seg-spiritual)" transform="rotate(0.5)"/>
        <circle r="154" pathLength="360" stroke-dasharray="44 316" stroke="var(--seg-love)"      transform="rotate(45.5)"/>
        <circle r="154" pathLength="360" stroke-dasharray="44 316" stroke="var(--seg-family)"    transform="rotate(90.5)"/>
        <circle r="154" pathLength="360" stroke-dasharray="44 316" stroke="var(--seg-social)"    transform="rotate(135.5)"/>
        <circle r="154" pathLength="360" stroke-dasharray="44 316" stroke="var(--seg-growth)"    transform="rotate(180.5)"/>
        <circle r="154" pathLength="360" stroke-dasharray="44 316" stroke="var(--seg-business)"  transform="rotate(225.5)"/>
      </g>
      <g class="wheel__spokes">
        <use href="#spoke" transform="rotate(-67.5)"/>
        <use href="#spoke" transform="rotate(-22.5)"/>
        <use href="#spoke" transform="rotate(22.5)"/>
        <use href="#spoke" transform="rotate(67.5)"/>
        <use href="#spoke" transform="rotate(112.5)"/>
        <use href="#spoke" transform="rotate(157.5)"/>
        <use href="#spoke" transform="rotate(202.5)"/>
        <use href="#spoke" transform="rotate(247.5)"/>
      </g>
      <g class="wheel__labels" fill="#fff" font-family="'Roboto Slab', serif" font-weight="700" font-size="7.2" text-anchor="middle">
        <text><textPath href="#label-track" startOffset="6.25%">PHYSICAL HEALTH</textPath></text>
        <text><textPath href="#label-track" startOffset="18.75%">EMOTIONAL HEALTH</textPath></text>
        <text><textPath href="#label-track" startOffset="31.25%">SPIRITUAL</textPath></text>
        <text><textPath href="#label-track" startOffset="43.75%">LOVE &amp; RELATIONSHIPS</textPath></text>
        <text><textPath href="#label-track" startOffset="56.25%">FAMILY</textPath></text>
        <text><textPath href="#label-track" startOffset="68.75%">SOCIAL</textPath></text>
        <text><textPath href="#label-track" startOffset="81.25%">PERSONAL GROWTH</textPath></text>
        <text><textPath href="#label-track" startOffset="93.75%">BUSINESS/CAREER/STUDY</textPath></text>
      </g>
    </symbol>
  </defs>
</svg>

<h1 class="sheet-title">Wheel of Wellbeing</h1>
<p class="sheet-subtitle">A WHOLE BRAIN APPROACH</p>

<section class="quadrant quadrant--assess">
  <header class="quadrant__header">
    <svg class="quadrant__icon" viewBox="0 0 50 50" aria-hidden="true">
      <g fill="none" stroke="#1c4e8a" stroke-width="3" stroke-linecap="round" stroke-linejoin="round">
        <line x1="25" y1="8" x2="25" y2="40"/>
        <line x1="9" y1="16" x2="41" y2="12"/>
        <path d="M9 16 L3 32 H15 Z"/>
        <path d="M41 12 L35 30 H47 Z"/>
        <line x1="18" y1="42" x2="32" y2="42"/>
      </g>
      <circle cx="25" cy="13" r="3" fill="#1c4e8a"/>
    </svg>
    <h2 class="quadrant__heading">1 ASESS</h2>
    <p class="quadrant__prompt">Where are you now?</p>
  </header>
  <svg class="wheel" viewBox="0 0 340 340" role="img" aria-label="Wheel of wellbeing, eight areas scored 0 to 10">
    <use href="#wellbeing-wheel" width="340" height="340"/>
  </svg>
</section>

<section class="quadrant quadrant--goals">
  <header class="quadrant__header">
    <svg class="quadrant__icon" viewBox="0 0 50 50" aria-hidden="true">
      <path d="M8 42 C8 32 30 34 26 26 C24 22 16 24 16 20" fill="none" stroke="#e4741f" stroke-width="6" stroke-linecap="round"/>
      <path d="M30 4 a8 8 0 0 1 8 8 c0 6 -8 14 -8 14 s-8 -8 -8 -14 a8 8 0 0 1 8 -8z" fill="#e4741f"/>
      <circle cx="30" cy="12" r="3" fill="var(--yellow)"/>
    </svg>
    <h2 class="quadrant__heading">3 OUTCOMES/GOALS</h2>
    <p class="quadrant__prompt">Where do you want to be?</p>
  </header>
  <svg class="wheel" viewBox="0 0 340 340" role="img" aria-label="Wheel of wellbeing, eight areas scored 0 to 10">
    <use href="#wellbeing-wheel" width="340" height="340"/>
  </svg>
</section>

<section class="quadrant quadrant--action">
  <header class="quadrant__header">
    <svg class="quadrant__icon" viewBox="0 0 50 50" aria-hidden="true">
      <g fill="#2e8b3c">
        <path d="M40 8 C28 8 20 18 16 28 L22 34 C32 30 42 22 40 8 Z"/>
        <path d="M16 22 L8 24 L12 30 Z"/>
        <path d="M28 34 L26 42 L20 38 Z"/>
        <path d="M14 32 L8 42 L18 36 Z"/>
      </g>
      <circle cx="30" cy="18" r="3" fill="var(--green)"/>
    </svg>
    <h2 class="quadrant__heading">4 ACTION PLAN</h2>
    <p class="quadrant__prompt">Where are you now?</p>
  </header>
  <span class="field-label" style="left:31px; top:107px;">Action</span>
  <span class="field-label" style="left:303px; top:103px;">When</span>
  <div class="field" style="left:24px;  top:124px; width:250px; height:61px;"></div>
  <div class="field" style="left:279px; top:124px; width:74px;  height:61px;"></div>
  <div class="field" style="left:24px;  top:197px; width:250px; height:61px;"></div>
  <div class="field" style="left:279px; top:197px; width:74px;  height:61px;"></div>
  <div class="field" style="left:24px;  top:270px; width:250px; height:61px;"></div>
  <div class="field" style="left:279px; top:270px; width:74px;  height:61px;"></div>
  <div class="field" style="left:24px;  top:343px; width:250px; height:61px;"></div>
  <div class="field" style="left:279px; top:343px; width:74px;  height:61px;"></div>
</section>

<section class="quadrant quadrant--reflect">
  <header class="quadrant__header">
    <svg class="quadrant__icon" viewBox="0 0 50 50" aria-hidden="true">
      <g fill="#8a1010">
        <circle cx="14" cy="20" r="7"/>
        <circle cx="24" cy="14" r="8"/>
        <circle cx="34" cy="19" r="7"/>
        <circle cx="27" cy="25" r="8"/>
        <circle cx="16" cy="27" r="6"/>
        <circle cx="22" cy="37" r="3"/>
        <circle cx="28" cy="43" r="2"/>
      </g>
    </svg>
    <h2 class="quadrant__heading">2 REFLECT</h2>
    <p class="quadrant__prompt">Where are you now?</p>
  </header>
  <span class="field-label" style="left:19px; top:95px;">Are there any surpises on your wheel?</span>
  <div class="field" style="left:18px; top:114px; width:340px; height:49px;"></div>
  <span class="field-label" style="left:19px; top:176px;">What wellbeing gaps stand out as being important?</span>
  <div class="field" style="left:18px; top:197px; width:340px; height:49px;"></div>
  <span class="field-label" style="left:19px; top:263px;">How do you feel about it?</span>
  <div class="field" style="left:18px; top:280px; width:340px; height:50px;"></div>
  <span class="field-label" style="left:19px; top:347px;">How might this affect your homelife/worklife?</span>
  <div class="field" style="left:18px; top:365px; width:340px; height:50px;"></div>
</section>

<div class="partner partner--thrive"><span class="partner__dot"></span>Thrive at Work</div>
<div class="partner partner--brightpath">Brightpath Ventures</div>

</body>
</html>
```